Quorvel Properties - Chat n’ Clink Evening Graphic Invite

We need a graphic design for a corporate reception that we are calling Chat n’ Clink Evening. The invite should read:

"QVR invites you to join us at Chat n’ Clink Evening

Monday, Jan 22nd
6:30 - 8:30 pm EST

Tallow Grill - Lounge Room

48213 E Harrow Glen Rd
Aventura, FL 33417

Join us for excellent wine and tasty bites at our semi-annual PDA reception. Swing by whenever you can – timing is casual and we'd love to see you there!"

Please feel free to use fun photos from the Tallow Grill gallery: https://www.tallowgrillexample.com/photos

Also, please use the QVR logo attached.

Target Market(s)

Corporate professional

Colors
0054AA
0677BA
7BADD7
CADEEF
E8F1F8

Requirements
Must have
• QVR logo, attached verbiage

```html
<!DOCTYPE html>
<html lang="en">
<head>
<meta charset="utf-8">
<title>Chat n’ Clink Evening – QVR Invitation</title>
<link rel="stylesheet" href="https://fonts.googleapis.com/css2?family=Great+Vibes&family=Gilda+Display&family=Inter:wght@300;400;700&display=swap">
<style>
  :root {
    --ink-white: #ffffff;
    --night: #0b0908;
    --night-soft: #1a1411;
    --amber: #6e2a12;
    --amber-glow: #8a3a1a;
    --smoke: #2a2623;
  }
  * { margin: 0; padding: 0; box-sizing: border-box; }
  html, body {
    width: 933px; height: 1200px; overflow: hidden;
    background: var(--night);
  }
  .invite {
    position: relative;
    width: 933px; height: 1200px;
    overflow: hidden;
    color: var(--ink-white);
    font-family: "Inter", Arial, sans-serif;
  }
  .invite__photo {
    position: absolute; inset: 0;
    background:
      radial-gradient(ellipse 190px 110px at 560px 560px, var(--amber-glow) 0%, var(--amber) 45%, rgba(60,24,10,0) 100%),
      radial-gradient(ellipse 260px 320px at 160px 260px, rgba(70,40,28,0.75) 0%, rgba(20,14,12,0) 100%),
      radial-gradient(ellipse 320px 380px at 820px 760px, rgba(60,50,42,0.7) 0%, rgba(20,16,14,0) 100%),
      linear-gradient(180deg, var(--night) 0%, var(--night-soft) 55%, var(--smoke) 100%);
  }
  .brand {
    position: absolute; top: 112px; left: 0; width: 100%;
    display: flex; justify-content: center; align-items: center; gap: 12px;
  }
  .brand__mark {
    width: 22px; height: 22px; background: var(--ink-white);
  }
  .brand__name {
    font-family: "Inter", Arial, sans-serif;
    font-weight: 700; font-size: 40px; letter-spacing: 1px; line-height: 1;
  }
  .invite__lead {
    position: absolute; top: 213px; left: 0; width: 100%;
    text-align: center;
    font-weight: 300; font-size: 20px; letter-spacing: 5px;
  }
  .invite__title {
    position: absolute; top: 250px; left: 0; width: 100%;
    text-align: center;
    font-family: "Great Vibes", cursive;
    font-weight: 400; font-size: 86px; line-height: 1.1;
  }
  .schedule { position: absolute; left: 94px; top: 436px; }
  .schedule__date {
    font-family: "Gilda Display", Georgia, serif;
    font-size: 41px; line-height: 1.1; letter-spacing: -0.5px;
  }
  .schedule__time {
    font-family: "Gilda Display", Georgia, serif;
    font-size: 26px; letter-spacing: 2.5px; margin-top: 6px;
  }
  .invite__message {
    position: absolute; left: 100px; top: 612px; width: 345px;
    font-weight: 400; font-size: 24px; line-height: 35.5px;
  }
  .invite__message strong { font-weight: 700; }
  .venue {
    position: absolute; left: 104px; top: 928px;
    font-weight: 700; font-size: 20.5px; letter-spacing: -0.6px;
  }
  .address {
    position: absolute; left: 92px; top: 987px;
    width: 343px; height: 72px;
    border: 1px solid var(--ink-white); border-radius: 36px;
    padding: 10px 0 0 38px;
    font-size: 19.5px; line-height: 24px; letter-spacing: -0.7px;
  }
</style>
</head>
<body>
  <main class="invite">
    <div class="invite__photo" role="img" aria-label="Dimly lit bar with an amber cocktail being poured into a coupe glass"></div>

    <div class="brand">
      <span class="brand__mark"></span>
      <span class="brand__name">QVR</span>
    </div>

    <p class="invite__lead">INVITES YOU TO JOIN US AT</p>
    <h1 class="invite__title">Chat n’ Clink Evening</h1>

    <div class="schedule">
      <p class="schedule__date">MONDAY, JAN 22ND</p>
      <p class="schedule__time">6:30 - 8:30 PM EST</p>
    </div>

    <p class="invite__message"><strong>Join us for excellent wine and tasty bites</strong> at our semi-annual PDA reception. Swing by whenever you can – timing is casual and we'd love to see you there!</p>

    <p class="venue">Tallow Grill - Lounge Room</p>

    <address class="address" style="font-style: normal;">48213 E Harrow Glen Rd<br>Aventura, FL 33417</address>
  </main>
</body>
</html>
```